Tampa, Florida based Real Estate company Business Cards

Need ideas for real estate business cards
Updates

Need extra days to review

Industry/Entity Type

Real Estate

Contact Information for Business Card

Space for image, space for logo, contact information space

Font styles to use
Sans Serif

Colors

Designer to choose colors to be used in the design.

Requirements
Must have
• Options to have duplicate content on the back of card for a team of agents.

```html
<!DOCTYPE html>
<html lang="en">
<head>
<meta charset="utf-8">
<title>Harbor Crest Realty – Business Card</title>
<link rel="stylesheet" href="https://fonts.googleapis.com/css2?family=Cinzel:wght@500;600&family=Arimo:wght@400&display=swap">
<style>
  :root {
    --navy: #1e1a52;
    --navy-deep: #181545;
    --silver: #a9a9ad;
    --grey-text: #9a9a9e;
    --white: #ffffff;
    --backdrop: #6e6e70;
  }
  * { margin: 0; padding: 0; box-sizing: border-box; }
  html, body { width: 1200px; height: 1095px; overflow: hidden; }
  body {
    background: var(--backdrop);
    position: relative;
    font-family: "Arimo", Arial, sans-serif;
  }
  .card {
    position: absolute;
    left: 180px;
    width: 840px;
    height: 480px;
    border-radius: 26px;
    overflow: hidden;
  }
  .card--front { top: 45px; background: var(--navy); }
  .card--back { top: 570px; background: var(--white); }

  .brand {
    position: absolute;
    text-align: center;
    font-family: "Cinzel", Georgia, serif;
    font-weight: 600;
    line-height: 1;
  }
  .brand__name { font-size: 64px; letter-spacing: 2px; }
  .brand__sub { font-size: 26px; letter-spacing: 14px; margin-top: 8px; }
  .brand__region { font-size: 18px; letter-spacing: 8px; margin-top: 6px; }
  .card--front .brand { left: 0; right: 0; top: 170px; color: var(--white); }
  .card--back .brand { left: 60px; width: 380px; top: 190px; color: var(--navy); }
  .card--back .brand__name { font-size: 48px; }
  .card--back .brand__sub { font-size: 20px; letter-spacing: 11px; }
  .card--back .brand__region { font-size: 14px; letter-spacing: 6px; }

  .contact {
    position: absolute;
    left: 470px;
    top: 62px;
    color: var(--navy);
  }
  .contact__name {
    font-family: "Cinzel", Georgia, serif;
    font-weight: 500;
    font-size: 32px;
    letter-spacing: 2px;
  }
  .contact__title { color: var(--grey-text); font-size: 17px; margin: 4px 0 12px; }
  .contact__line { font-size: 18px; line-height: 28px; }
  .contact__list { list-style: none; margin-top: 8px; }
  .contact__item {
    display: flex; align-items: center; gap: 10px;
    font-size: 18px; line-height: 30px;
  }
  .contact__icon { width: 16px; height: 16px; flex: none; }

  .wave { position: absolute; left: 0; top: 0; }
  .social {
    position: absolute;
    left: 480px; top: 418px;
    display: flex; gap: 14px; list-style: none;
  }
  .social__dot {
    width: 26px; height: 26px; border-radius: 50%;
    background: var(--white);
  }
</style>
</head>
<body>

  <section class="card card--front" aria-label="Card front">
    <div class="brand">
      <div class="brand__name">HARBOR CREST</div>
      <div class="brand__sub">REALTY</div>
      <div class="brand__region">TAMPA BAY</div>
    </div>
  </section>

  <section class="card card--back" aria-label="Card back">
    <svg class="wave" width="840" height="480" viewBox="0 0 840 480" aria-hidden="true">
      <path d="M0,470 C220,420 470,355 840,330" fill="none" stroke="#a9a9ad" stroke-width="6"/>
      <path d="M0,480 C230,440 480,378 840,352 L840,480 Z" fill="#1e1a52"/>
    </svg>

    <div class="brand">
      <div class="brand__name">HARBOR CREST</div>
      <div class="brand__sub">REALTY</div>
      <div class="brand__region">TAMPA BAY</div>
    </div>

    <div class="contact">
      <div class="contact__name">DALE MORROW</div>
      <div class="contact__title">Managing Director</div>
      <div class="contact__line">1420 W Palm Shore Ave</div>
      <div class="contact__line">Tampa, FL 33611</div>
      <ul class="contact__list">
        <li class="contact__item">
          <svg class="contact__icon" viewBox="0 0 16 16" aria-hidden="true"><path d="M3 1.5l2.5 0 1 3.5-1.6 1.2a8 8 0 0 0 4.9 4.9L11 9.5l3.5 1v2.5A1.5 1.5 0 0 1 13 14.5 11.5 11.5 0 0 1 1.5 3 1.5 1.5 0 0 1 3 1.5z" fill="#9a9a9e"/></svg>
          (813) 555 - 0147
        </li>
        <li class="contact__item">
          <svg class="contact__icon" viewBox="0 0 16 16" aria-hidden="true"><rect x="1" y="3" width="14" height="10" rx="1" fill="#9a9a9e"/><path d="M1.5 3.5L8 9l6.5-5.5" fill="none" stroke="#fff" stroke-width="1.3"/></svg>
          hello@harborcrestrealty.com
        </li>
        <li class="contact__item">
          <svg class="contact__icon" viewBox="0 0 16 16" aria-hidden="true"><circle cx="8" cy="8" r="6.5" fill="none" stroke="#9a9a9e" stroke-width="1.4"/><ellipse cx="8" cy="8" rx="2.8" ry="6.5" fill="none" stroke="#9a9a9e" stroke-width="1.2"/><path d="M1.5 8h13" stroke="#9a9a9e" stroke-width="1.2"/></svg>
          harborcrestrealty.com
        </li>
      </ul>
    </div>

    <ul class="social" aria-label="Social media links">
      <li class="social__dot"></li>
      <li class="social__dot"></li>
      <li class="social__dot"></li>
      <li class="social__dot"></li>
    </ul>
  </section>

</body>
</html>
```